FUN and creative designs WANTED! Mobile Marketing Start-up Company

Website design needed.

- QB is a full service mobile marketing agency in existence to help connect companies with their audience on unwired devices (Smartphone and tablets).

- QB is a start-up business with no current website looking to make a solid, memorable first impression.
Updates

Please take into consideration the following two points from our brief:

-  sense of humour and fun. Showing that mobile marketing for your business can be easy, interesting, and not just for big companies.

- a little ‘left of centre’ (i.e. NOT corporate!)

Thanks!

Please don't use black as a back groud. 

Target Market(s)

Primarily Media Agencies and Direct clients of all business types

Industry/Entity Type

Marketing

Requirements
Must have
• •The website should be: simple, clean yet a little ‘left of centre’ (i.e. NOT corporate!)
•Colour-in-line with QB logo (Black, Grey and orange: RBG: 255, 59, 0)
•Font: Arial and Aller Bold as per logo
•The website needs to show the charter of the business- sense of humour and fun. Showing that mobile marketing for your business can be easy, interesting, and not just for big companies.

What pages are required:
-Home Page
-Why Mobile
-Why Quill
-Services
-Contact

* For initial submission only a home page and one sub-page is require as the other pages will work from the same template

* Coding would be great but not a essential
Nice to have
• Please suggest some stock photos for the website
Should not have
• Please review all attached documents:
* Full brief
* Logo files
* Web copy

```html
<!DOCTYPE html>
<html lang="en">
<head>
<meta charset="utf-8">
<title>Quill Unwired — Home</title>
<link rel="stylesheet" href="https://fonts.googleapis.com/css2?family=Righteous&family=Original+Surfer&family=Comfortaa:wght@400;700&display=block">
<style>
  :root {
    --orange: #ff3b00;
    --brown: #3a2a0e;
    --sun: #f7d24a;
    --sky: #d3f1ee;
    --marketer: #e8474b;
    --agency: #45a7c0;
    --cream: #f5efe0;
    --dash: #3aa3c6;
    --cloud: #f2c544;
    --retro: "Righteous", "Original Surfer", cursive;
  }
  * { box-sizing: border-box; margin: 0; padding: 0; }
  html, body { width: 865px; height: 1200px; overflow: hidden; }
  body {
    position: relative;
    font-family: "Comfortaa", sans-serif;
    color: var(--brown);
    background:
      radial-gradient(circle at 495px 160px, rgba(255,236,110,.95) 0, rgba(250,214,80,.8) 160px, rgba(245,215,110,.35) 420px, rgba(245,215,110,0) 620px),
      linear-gradient(180deg, #f6dd8a 0%, #f0e4a4 38%, #dcefd8 62%, var(--sky) 100%);
  }
  .main-nav { position: absolute; top: 20px; left: 0; width: 100%; }
  .main-nav a {
    position: absolute;
    font-family: var(--retro);
    font-size: 28px;
    color: var(--brown);
    text-decoration: none;
    letter-spacing: .5px;
  }
  .main-nav a.is-active { color: var(--orange); }

  .retro { font-family: var(--retro); }

  .queries { position: absolute; left: 64px; top: 96px; width: 160px; height: 110px; }
  .queries-number {
    position: absolute; left: 80px; top: 180px;
    font-family: Arial, sans-serif; font-size: 17px; color: var(--brown);
  }

  .brand {
    position: absolute; left: 420px; top: 140px;
    display: flex; align-items: center; gap: 10px;
  }
  .brand-mark { width: 30px; height: 30px; border-radius: 50%; background: var(--orange); }
  .brand-name { font-family: Arial, sans-serif; font-weight: 700; font-size: 38px; color: var(--brown); }

  .hero-visual {
    position: absolute; left: 282px; top: 250px; width: 400px; height: 236px;
    border-radius: 50%;
    background: radial-gradient(ellipse at center, rgba(255,250,200,.95) 0, rgba(255,228,110,.85) 35%, rgba(247,205,70,.45) 60%, rgba(247,210,80,0) 75%);
  }

  .headline {
    position: absolute; left: 0; width: 100%; text-align: center;
    font-family: var(--retro); font-weight: 400; line-height: 1; letter-spacing: 1px;
  }
  .headline-primary { top: 510px; font-size: 40px; color: var(--brown); }
  .headline-accent { top: 566px; font-size: 42px; color: var(--orange); }

  .intro {
    position: absolute; left: 50px; top: 626px; width: 760px; height: 84px; overflow: hidden;
    font-size: 18px; line-height: 28px; letter-spacing: -.3px; color: #2a2418;
  }

  .know-more { position: absolute; left: 684px; top: 726px; width: 136px; height: 70px; }
  .know-more span {
    position: absolute; left: 0; top: 14px; width: 132px; text-align: center;
    font-family: var(--retro); font-size: 19px; color: var(--brown);
  }

  .audience { position: absolute; top: 812px; width: 260px; height: 240px; text-decoration: none; }
  .audience-marketer { left: 89px; }
  .audience-agency { left: 465px; }

  .site-footer { position: absolute; left: 40px; top: 1087px; width: 781px; height: 78px;
    border-top: 3px dashed var(--dash); border-bottom: 3px dashed var(--dash); }
  .copyright {
    position: absolute; left: 15px; top: 27px;
    font-family: var(--retro); font-size: 15px; color: var(--brown);
  }
  .copyright a { color: var(--dash); text-decoration: none; }
  .social { position: absolute; right: 14px; top: 16px; display: flex; align-items: center; gap: 12px; }
  .social-label { font-family: "Comfortaa", sans-serif; font-size: 19px; color: var(--orange); margin-right: 18px; }
  .social-tile { width: 38px; height: 38px; border: 2px solid #2d3a55; border-radius: 4px; background: #e9eef3; }
</style>
</head>
<body>
  <nav class="main-nav">
    <a class="is-active" href="#" style="left:37px">Home</a>
    <a href="#" style="left:158px">Why Mobile</a>
    <a href="#" style="left:360px">Why Quill</a>
    <a href="#" style="left:538px">Services</a>
    <a href="#" style="left:707px">Contact</a>
  </nav>

  <div class="queries">
    <svg width="160" height="110" viewBox="0 0 160 110" aria-hidden="true">
      <defs><path id="queries-arc" d="M14 70 A66 58 0 0 1 146 70"/></defs>
      <text class="retro" font-size="19" fill="#3a2a0e">
        <textPath href="#queries-arc" startOffset="50%" text-anchor="middle">ANY QUERIES</textPath>
      </text>
      <circle cx="80" cy="60" r="20" fill="#e81e1e"/>
      <path d="M72 50 q-3 10 8 20 q4 3 8 1 l-3-5 q-3 1-5-2 q-4-5-2-8 l-3-5z" fill="#fff"/>
    </svg>
  </div>
  <div class="queries-number">0000 000 0000</div>

  <div class="brand">
    <span class="brand-mark"></span>
    <span class="brand-name">Quill</span>
  </div>

  <div class="hero-visual" role="img" aria-label="Glowing smartphone lying on its side with sparkles"></div>

  <h1 class="headline headline-primary">WE'RE ALL GOING UNWIRED.</h1>
  <h2 class="headline headline-accent">ISN'T IT TIME YOU CONNECTED.</h2>

  <p class="intro">Your customers are less wired, more savvy, and more in control than ever before. They're untied to (broadcast) programming schedules, un-tethered to local content and unbridled in their choice of doing what they want when they want.</p>

  <a class="know-more" href="#">
    <svg width="136" height="70" viewBox="0 0 136 70" aria-hidden="true">
      <ellipse cx="66" cy="26" rx="64" ry="24" fill="var(--cloud)"/>
      <ellipse cx="46" cy="56" rx="14" ry="5" fill="var(--cloud)"/>
      <ellipse cx="28" cy="65" rx="7" ry="3" fill="var(--cloud)"/>
    </svg>
    <span>know more</span>
  </a>

  <a class="audience audience-marketer" href="#">
    <svg width="260" height="240" viewBox="0 0 260 240" aria-label="Are you a marketer?">
      <defs><path id="marketer-arc" d="M24 160 A108 108 0 1 1 236 160"/></defs>
      <text class="retro" font-size="25" fill="var(--orange)" letter-spacing="1">
        <textPath href="#marketer-arc" startOffset="50%" text-anchor="middle">ARE YOU A MARKETER?</textPath>
      </text>
      <circle cx="130" cy="136" r="88" fill="var(--cream)"/>
      <circle cx="130" cy="136" r="74" fill="var(--marketer)"/>
      <circle cx="130" cy="136" r="62" fill="none" stroke="#fff" stroke-width="2" stroke-dasharray="3 9"/>
      <rect x="117" y="118" width="26" height="34" rx="3" fill="#b8262a"/>
      <rect x="121" y="122" width="18" height="7" fill="#e8474b"/>
    </svg>
  </a>

  <a class="audience audience-agency" href="#">
    <svg width="260" height="240" viewBox="0 0 260 240" aria-label="Are you an agency?">
      <defs><path id="agency-arc" d="M24 160 A108 108 0 1 1 236 160"/></defs>
      <text class="retro" font-size="25" fill="var(--agency)" letter-spacing="1">
        <textPath href="#agency-arc" startOffset="50%" text-anchor="middle">ARE YOU AN AGENCY?</textPath>
      </text>
      <circle cx="130" cy="136" r="88" fill="var(--cream)"/>
      <circle cx="130" cy="136" r="74" fill="var(--agency)"/>
      <circle cx="130" cy="136" r="62" fill="none" stroke="#fff" stroke-width="2" stroke-dasharray="3 9"/>
      <rect x="121" y="118" width="18" height="10" rx="3" fill="none" stroke="#1f6f86" stroke-width="4"/>
      <rect x="112" y="126" width="36" height="26" rx="3" fill="#1f6f86"/>
    </svg>
  </a>

  <footer class="site-footer">
    <p class="copyright">© ALL RIGHTS RESERVED, <a href="#">QUILL UNWIRED.COM.AU</a></p>
    <div class="social">
      <span class="social-label">Catch Us</span>
      <span class="social-tile" aria-label="Social profile"></span>
      <span class="social-tile" aria-label="Social profile"></span>
    </div>
  </footer>
</body>
</html>
```